1 Page InfoGraphic "5 Steps to Bright Harbor"

The finished product will be an 8 1/2 x 11 infographic.
This page will contain the imagery and words to communicate three things:
#1. That "Abundance" and "BrightHarbor" work inter-dependently. Having financial and time abundance provides more resources with which to pursue BrightHarbor, and the more BrightHarbor you have the more you'll experience abundance----which then just magnifies BrightHarbor which leads to experiencing more abundance..............the two concepts work together almost like a perpetual motion machine.
#2. Steady Porch Paycheck. This is a simple concept......likely imagery is a Civic Parcel mailbox with the flag up, and then lines interposed across the mailbox image to fill in the blank for the amount of Steady Porch Paycheck from
-His Social Security
-Her Social Security
-Pension #1
-Pension #2
-PIRA
-Investments
#3. The five step process. This imagery will show forward motion through the five steps
1. Position
2. Project
3. Protect
4. Payoff
5. Perpetuate
Once we've decided on the forward-motion imagery illustrating those steps, then we'll have a "check list" of items to be completed under each step, so we can check them off, or put a date by them as they are completed.
IN THE END this one page document will illustrate what it's like working with our firm, and how we take the client through these five steps, securing Steady Porch Paycheck so that the client is free financially and mentally to pursue abundance (however they define that) and experience BrightHarbor.
The accompanying attached document takes you through the "Conversation" that we'll have with the prospective client while we're walking them through the one-page document that you will have designed.
Once we have finished design of the one pager, the elements from the design will be incorporated into our website, in PowerPoint presentations, etc. So we'll need ongoing access to the images in various form, and may from time-to-time come back to the designer to tweak or add on.
(I have attached both stacked and horizontal logos. Somewhere on the page you'll want the logo.)
Updates
Target Market(s)
Adults age 50-70 years
Industry/Entity Type
Product
Requirements
Must have
- 1. Open Horizon / Bright Harbor
- 2. Five Steps to Bright Harbor

```html
<!DOCTYPE html>
<html lang="en">
<head>
<meta charset="utf-8">
<title>5 Steps to Bright Harbor</title>
<link href="https://fonts.googleapis.com/css2?family=Questrial&family=Dosis:wght@500&display=swap" rel="stylesheet">
<style>
  :root{
    --page-bg:#e9ecef;
    --paper:#ffffff;
    --blue:#1f7ccc;
    --blue-deep:#1769b3;
    --lime:#c5e03b;
    --white:#ffffff;
    --navy:#1c3f72;
    --figure:#2a5f96;
    --figure-light:#6fa6d8;
  }
  *{margin:0;padding:0;box-sizing:border-box}
  html,body{width:1200px;height:1200px;overflow:hidden;background:var(--page-bg)}
  .flyer{
    position:absolute;left:160px;top:30px;width:881px;height:1140px;
    background:linear-gradient(180deg,var(--blue) 0%,var(--blue-deep) 100%);
    font-family:"Questrial",sans-serif;color:var(--white);overflow:hidden;
    box-shadow:0 6px 22px rgba(0,0,0,.18);
  }
  .flyer-art{position:absolute;left:0;top:0}
  .brand{
    position:absolute;left:0;right:0;top:48px;display:flex;justify-content:center;align-items:center;gap:12px;
    color:var(--navy);
  }
  .brand-mark{width:34px;height:34px;background:var(--navy)}
  .brand-name{font-size:34px;line-height:1;letter-spacing:1px}
  .brand-tag{font-size:14px;display:block;margin-top:4px;letter-spacing:.5px}
  .step-label{
    position:absolute;width:124px;text-align:center;font-family:"Dosis",sans-serif;font-weight:500;
    font-size:30px;color:var(--lime);letter-spacing:.5px;line-height:1;
  }
  .heading{color:var(--lime);font-size:21px;line-height:1.25;position:absolute;font-weight:400}
  .body-copy{font-size:16px;line-height:1.3;position:absolute}
  .checklist{position:absolute;list-style:none;font-size:22px}
  .checklist li{display:flex;align-items:center;gap:14px;height:30.5px}
  .box{width:15px;height:15px;border:2px solid var(--lime);flex:none}
  .steps-list{position:absolute;left:214px;top:984px;display:grid;grid-template-columns:192px 170px;row-gap:10px;list-style:none;font-size:24px}
  .steps-list li{display:flex;align-items:center;gap:12px;height:32px}
  .steps-list .box{width:22px;height:22px}
  .figure{position:absolute;border-radius:30px 30px 8px 8px;background:linear-gradient(180deg,var(--figure-light),var(--figure))}
  .bubble-name{position:absolute;color:var(--navy);font-size:13px;text-align:center}
</style>
</head>
<body>
<main class="flyer">
  <svg class="flyer-art" width="881" height="1140" viewBox="0 0 881 1140" aria-hidden="true">
    <polygon points="0,0 881,0 881,101 441,169 0,101" fill="var(--paper)"/>
    <path d="M97 352 V422 Q97 437 112 437 H807 Q822 437 822 452 V526 Q822 541 807 541 H82 Q67 541 67 556 V935 Q67 950 82 950 H642 Q657 950 657 935 V865"
          fill="none" stroke="var(--white)" stroke-width="5" stroke-dasharray="0 11" stroke-linecap="round"/>
    <circle cx="97" cy="288" r="62" fill="var(--blue)" stroke="var(--white)" stroke-width="5"/>
    <circle cx="485" cy="546" r="62" fill="var(--blue)" stroke="var(--white)" stroke-width="5"/>
    <circle cx="657" cy="803" r="62" fill="var(--blue)" stroke="var(--white)" stroke-width="5"/>
    <circle cx="227" cy="275" r="4" fill="var(--white)"/>
    <circle cx="240" cy="270" r="6" fill="var(--white)"/>
    <ellipse cx="300" cy="250" rx="50" ry="36" fill="var(--white)"/>
    <ellipse cx="802" cy="838" rx="62" ry="42" fill="var(--white)"/>
    <polygon points="770,868 760,900 795,876" fill="var(--white)"/>
    <text x="254" y="350" font-family="Questrial,sans-serif" font-size="52" fill="var(--white)">$</text>
    <circle cx="340" cy="338" r="15" fill="none" stroke="var(--white)" stroke-width="9" stroke-dasharray="6 4"/>
    <circle cx="338" cy="398" r="15" fill="none" stroke="var(--white)" stroke-width="9" stroke-dasharray="6 4"/>
    <rect x="386" y="395" width="30" height="20" rx="2" fill="none" stroke="var(--white)" stroke-width="3"/>
    <line x1="401" y1="415" x2="401" y2="423" stroke="var(--white)" stroke-width="3"/>
    <circle cx="706" cy="583" r="17" fill="none" stroke="var(--white)" stroke-width="10" stroke-dasharray="6 4"/>
    <text x="632" y="635" font-family="Questrial,sans-serif" font-size="38" fill="var(--white)">$</text>
    <circle cx="710" cy="667" r="16" fill="none" stroke="var(--white)" stroke-width="3"/>
    <polyline points="710,657 710,667 718,671" fill="none" stroke="var(--white)" stroke-width="3"/>
    <g fill="var(--white)">
      <rect x="617" y="650" width="6" height="34"/>
      <rect x="627" y="665" width="6" height="19"/>
      <rect x="637" y="658" width="6" height="26"/>
      <rect x="647" y="672" width="6" height="12"/>
    </g>
    <circle cx="680" cy="470" r="14" fill="none" stroke="var(--white)" stroke-width="4"/>
    <rect x="673" y="486" width="14" height="8" fill="var(--white)"/>
    <polygon points="760,475 790,458 798,462 776,478 784,494 778,496 768,482 755,488" fill="var(--white)"/>
  </svg>

  <div class="brand">
    <span class="brand-mark"></span>
    <span class="brand-name">Keelstone<span class="brand-tag">Tax &amp; Investment Advisors</span></span>
  </div>

  <div class="bubble-name" style="left:250px;top:242px;width:100px">Keelstone</div>
  <div class="bubble-name" style="left:752px;top:830px;width:100px">Keelstone</div>

  <div class="step-label" style="left:35px;top:273px">STEP 1</div>
  <div class="step-label" style="left:423px;top:531px">STEP 2</div>
  <div class="step-label" style="left:595px;top:788px">STEP 3</div>

  <div class="figure" role="img" aria-label="Illustrated advisor standing" style="left:162px;top:262px;width:56px;height:205px"></div>
  <div class="figure" role="img" aria-label="Illustrated advisor pointing" style="left:548px;top:616px;width:58px;height:110px"></div>
  <div class="figure" role="img" aria-label="Illustrated advisor giving thumbs up" style="left:690px;top:890px;width:110px;height:232px"></div>
  <div class="figure" role="img" aria-label="Illustration of two people shaking hands" style="left:60px;top:902px;width:132px;height:211px"></div>
  <div class="figure" role="img" aria-label="Illustration of a person working at a desk" style="left:566px;top:986px;width:104px;height:139px;border-radius:8px"></div>

  <h2 class="heading" style="left:410px;top:195px;width:440px">That "Abundance" and "BrightHarbor"<br>work inter-dependently.</h2>
  <p class="body-copy" style="left:410px;top:252px;width:410px">Having financial and time abundance provides more resources with which to pursue BrightHarbor, and the more BrightHarbor you have the more you'll experience abundance----which then just magnifies BrightHarbor which leads to experiencing more abundance.............the two concepts work together almost like a perpetual motion machine.</p>

  <h2 class="heading" style="left:83px;top:576px;width:200px">Steady Porch Paycheck</h2>
  <p class="body-copy" style="left:83px;top:632px;width:205px">This is a simple concept......likely imagery is a Civic Parcel mailbox with the flag up, and then lines interposed across the mailbox image to fill in the blank for the amount of Steady Porch Paycheck from</p>

  <ul class="checklist" style="left:314px;top:629px">
    <li><span class="box"></span>His Social Security</li>
    <li><span class="box"></span>Her Social Security</li>
    <li><span class="box"></span>Pension #1</li>
    <li><span class="box"></span>Pension #2</li>
    <li><span class="box"></span>PIRA</li>
    <li><span class="box"></span>Investments</li>
  </ul>

  <h2 class="heading" style="left:320px;top:869px">The five step process.</h2>
  <p class="body-copy" style="left:320px;top:898px;width:270px">This imagery will show forward motion through the five steps</p>

  <ul class="steps-list">
    <li><span class="box"></span>1. Position</li>
    <li><span class="box"></span>2. Project</li>
    <li><span class="box"></span>3. Protect</li>
    <li><span class="box"></span>4. Payoff</li>
    <li><span class="box"></span>5. Perpetuate</li>
  </ul>
</main>
</body>
</html>
```